Business is backhoe and truck hire. As the title indicates, we dig dirt. Colours preferred are charcoal, red and or orange. Would like a backhoe on the card,possibly a designs with the silhouette of the machine in the background. I We would like to incorporate a large tick in the title for solutions. I thought it could be part of the "W" . Our shirts are Black polo's with orange lines around sleeves and sides. We are a new business in rural Qld, happy to do the smaller jobs that others wont.

Industry/Entity Type

Business

Contact Information for Business Card

Tall Creek Groundworks Services

Backhoe and Truck Hire
ABN:81264950173

Peter Holloway
PH: 0491 732 580
PH: 0493 618 204
PH: 4683 1057 a/h

email: tcgservices@mailbox-example.net

```html
<!DOCTYPE html>
<html lang="en">
<head>
<meta charset="utf-8">
<title>Tall Creek Groundworks Services – Business Card</title>
<link rel="stylesheet" href="https://fonts.googleapis.com/css2?family=Alfa+Slab+One&family=Tinos:wght@400;700&display=swap">
<style>
  :root {
    --soil-dark: #5a4330;
    --soil-mid: #7d6148;
    --soil-light: #977a5d;
    --card-orange: #f6891f;
    --ink: #1c1a18;
    --machine: #231f1c;
  }
  * { margin: 0; padding: 0; box-sizing: border-box; }
  html, body { width: 1200px; height: 693px; overflow: hidden; }
  body { background: var(--soil-mid); }
  .card {
    position: relative;
    width: 1200px;
    height: 693px;
    overflow: hidden;
  }
  .soil-backdrop {
    position: absolute;
    inset: 0;
    background: radial-gradient(ellipse at 40% 40%, var(--soil-light), var(--soil-mid) 55%, var(--soil-dark));
  }
  .panel {
    position: absolute;
    left: 45px;
    top: 47px;
    width: 1106px;
    height: 600px;
    background: var(--card-orange);
    color: var(--ink);
  }
  .business-name {
    position: absolute;
    left: 0;
    right: 0;
    top: 12px;
    text-align: center;
    font-family: "Alfa Slab One", serif;
    font-weight: 400;
    font-size: 76px;
    line-height: 84px;
    letter-spacing: 0.5px;
  }
  .business-name span { display: block; }
  .tagline {
    position: absolute;
    left: 0;
    right: 0;
    top: 207px;
    text-align: center;
    font-family: "Tinos", serif;
    font-size: 40px;
    letter-spacing: 1px;
  }
  .machine-art {
    position: absolute;
    left: 9px;
    top: 337px;
    width: 511px;
    height: 263px;
    background: var(--machine);
    border-radius: 6px 40px 0 0;
  }
  .contact {
    position: absolute;
    right: 5px;
    top: 318px;
    text-align: right;
  }
  .contact-name {
    font-family: "Alfa Slab One", serif;
    font-size: 48px;
    line-height: 60px;
    margin-bottom: 2px;
  }
  .contact-line {
    font-family: "Tinos", serif;
    font-weight: 700;
    font-size: 37px;
    line-height: 53px;
  }
  .contact-line.email { font-size: 33px; }
</style>
</head>
<body>
  <div class="card">
    <div class="soil-backdrop" role="img" aria-label="Photograph of loose brown dirt filling the card background"></div>
    <div class="panel">
      <h1 class="business-name"><span>Tall Creek</span><span>Groundworks Services</span></h1>
      <p class="tagline">Backhoe and Truck Hire</p>
      <div class="machine-art" role="img" aria-label="Black silhouette illustration of a mini excavator tipping soil from its bucket"></div>
      <div class="contact">
        <p class="contact-name">Peter Holloway</p>
        <p class="contact-line">Phone: 0491 732 580</p>
        <p class="contact-line">Phone: 0493 618 204</p>
        <p class="contact-line email">tcgservices@mailbox-example.net</p>
        <p class="contact-line">ABN:81264950173</p>
      </div>
    </div>
  </div>
</body>
</html>
```